Astrology Reading Website to attract clients

I need a website for my astrology practice. My business name is Willow Tide Astrology. I will need a page the following pages: About, Readings, Booking, Contact, and Blog. I will need full figma or figma-like mockups of pages along with assets. I will need both desktop and mobile designs.
I like creams, dark blues and greens. I am fine with planets or other astrology symbolism.

Target Market(s)

new age, spiritual

Industry/Entity Type

Holistic, spiritual

Number of Pages Required

3 page

Colors
0054AA
0677BA
7BADD7
CADEEF
E8F1F8

Requirements
Nice to have
• calm and grounded backgrounds

```html
<!DOCTYPE html>
<html lang="en">
<head>
<meta charset="utf-8">
<title>Willow Tide Astrology</title>
<link href="https://fonts.googleapis.com/css2?family=Cinzel:wght@400;500&family=Poppins:wght@400;500&display=swap" rel="stylesheet">
<style>
:root{
  --navy:#0a1052;
  --navy-deep:#050938;
  --midnight:#060b30;
  --violet:#3b1675;
  --violet-soft:#5a2a9e;
  --cream:#fdf6d2;
  --cream-line:#f6efc4;
  --ink:#17163f;
  --white:#ffffff;
  --muted:#c9c8e8;
  --card-line:rgba(255,255,255,.55);
  --head:"Cinzel",Georgia,serif;
  --body:"Poppins",Arial,sans-serif;
}
*{box-sizing:border-box;margin:0;padding:0}
html,body{width:1200px;height:4839px;overflow:hidden}
body{
  position:relative;font-family:var(--body);color:var(--white);
  background:
    radial-gradient(circle at 355px 235px,rgba(120,160,255,.9) 0 4px,transparent 6px),
    radial-gradient(circle at 965px 895px,rgba(160,200,255,.9) 0 7px,transparent 10px),
    radial-gradient(circle at 672px 770px,rgba(255,150,255,.8) 0 5px,transparent 8px),
    radial-gradient(circle at 1170px 2455px,rgba(150,220,255,.8) 0 6px,transparent 9px),
    radial-gradient(circle at 1145px 3540px,rgba(150,220,255,.7) 0 5px,transparent 8px),
    radial-gradient(ellipse 520px 380px at 200px 260px,rgba(70,60,190,.55),transparent 70%),
    radial-gradient(ellipse 420px 360px at 520px 1480px,rgba(120,90,220,.35),transparent 70%),
    radial-gradient(ellipse 600px 500px at 1000px 300px,rgba(40,70,200,.5),transparent 70%),
    linear-gradient(180deg,var(--navy) 0,#101467 700px,var(--navy) 1600px,var(--navy-deep) 3200px,var(--navy) 4000px);
}
.abs{position:absolute}
.btn{
  position:absolute;display:flex;align-items:center;justify-content:center;gap:14px;
  background:var(--cream);color:var(--ink);border-radius:40px;font-family:var(--body);
  font-weight:500;text-decoration:none;
}
.btn svg{width:10px;height:14px}
.divider{position:absolute;height:2px;background:linear-gradient(90deg,transparent,var(--cream-line) 20%,var(--cream-line) 80%,transparent)}
.divider::after{content:"";position:absolute;left:50%;top:-4px;width:10px;height:10px;margin-left:-5px;border-radius:50%;background:var(--cream)}
.section-title{position:absolute;font-family:var(--head);font-weight:400;letter-spacing:1px;color:var(--cream)}

/* header */
.site-header{position:absolute;left:0;top:0;width:1200px;height:132px;background:var(--navy-deep)}
.brand{position:absolute;left:66px;top:62px;font-family:var(--head);font-size:20px;letter-spacing:.5px;color:var(--white)}
.main-nav{position:absolute;top:57px;left:561px;display:flex;gap:0;font-size:12px}
.main-nav a{color:var(--white);text-decoration:none;position:absolute;white-space:nowrap}
.main-nav a.active::after{content:"";position:absolute;left:0;right:0;bottom:-10px;height:2px;background:var(--white)}
.nav-contact{left:1020px;top:51px;width:113px;height:34px;font-size:12px}

/* hero */
.hero-title{left:64px;top:306px;font-size:38px;color:var(--white)}
.hero-sub{position:absolute;left:64px;top:388px;width:470px;font-size:23px;line-height:32px}
.hero-cta{left:66px;top:516px;width:231px;height:66px;font-size:22px}
.hero-wheel{left:584px;top:216px;width:582px;height:582px;border-radius:50%;
  background:radial-gradient(circle,#5a3ee8 0,#3a2dbd 45%,#2622a0 70%,#6f6bff 96%,#fff 100%);
  box-shadow:0 0 60px rgba(120,110,255,.7)}
.swoosh{position:absolute;left:0;width:1200px}

/* about */
.about-ring{left:91px;top:1018px;width:506px;height:506px;border-radius:50%;border:2px solid var(--cream-line)}
.about-art{left:109px;top:1036px;width:470px;height:470px;border-radius:50%;
  background:radial-gradient(circle,#fbf6e6 0,#f1e8cf 70%,#e4d7b3 100%)}
.about-title{left:657px;top:1096px;font-size:46px}
.about-text{position:absolute;left:655px;top:1217px;width:410px;font-size:13.5px;line-height:24px;color:var(--white)}
.about-cta{left:650px;top:1384px;width:154px;height:49px;font-size:16px}

/* fate band */
.fate-band{left:-160px;top:1568px;width:1520px;height:883px;border-radius:50%;
  background:radial-gradient(ellipse at center,#4a1c8c 0,#3a1573 45%,#2a0f5e 80%,rgba(30,10,80,.4) 100%)}
.fate-title{left:0;top:1846px;width:1200px;text-align:center;font-size:46px;line-height:64px;color:var(--cream)}
.fate-text{position:absolute;left:210px;top:2050px;width:780px;text-align:center;font-size:17.5px;line-height:25px;color:var(--white)}
.fate-cta{left:453px;top:2147px;width:294px;height:47px;font-size:16px}

/* services */
.card{position:absolute;top:2689px;width:329px;height:344px;border:1.5px solid var(--card-line);border-radius:22px;text-align:center;
  background:linear-gradient(180deg,rgba(20,25,100,.4),rgba(10,14,70,.6))}
.card-icon{position:absolute;left:115px;top:50px;width:100px;height:100px;border-radius:50%;
  background:radial-gradient(circle,rgba(255,255,255,.55) 0,rgba(255,255,255,.15) 45%,transparent 70%)}
.card h3{position:absolute;left:20px;right:20px;top:176px;font-weight:500;font-size:19px;line-height:26px;color:var(--cream)}
.card p{position:absolute;left:26px;right:26px;font-size:12.5px;line-height:20px;color:var(--white)}
.services-cta{left:522px;top:3086px;width:154px;height:48px;font-size:16px}

/* blog */
.post-img{position:absolute;top:3435px;width:323px;height:289px}
.post-body{position:absolute;top:3681px;width:292px;height:229px;background:var(--midnight);border-radius:0 0 10px 10px;padding:30px 28px}
.post-date{display:flex;align-items:center;gap:7px;font-size:10px}
.post-date i{width:10px;height:10px;background:var(--muted);display:block}
.post-body h3{margin-top:12px;font-size:12px;font-weight:500;line-height:14px;color:var(--white)}
.post-body p{margin-top:14px;font-size:12px;line-height:19px;color:var(--muted)}
.post-more{margin-top:22px;display:inline-block;background:var(--cream);color:var(--ink);font-size:9px;padding:4px 12px;border-radius:10px;font-weight:500}

/* contact */
.contact-bg{left:0;top:3990px;width:1200px;height:560px;
  background:radial-gradient(ellipse at 60% 40%,#3d1879 0,#2b1163 55%,#1b0c4a 100%)}
.contact-title{left:70px;top:4108px;font-size:44px}
.contact-intro{position:absolute;left:70px;top:4206px;font-size:14.5px;line-height:24px}
.field{position:absolute;background:var(--white);color:#777;font-size:12px;padding-left:16px;display:flex;align-items:center}
.field.msg{align-items:flex-start;padding-top:20px}
.submit{left:66px;top:4503px;width:150px;height:44px;font-size:16px}
.contact-orb{left:704px;top:4122px;width:432px;height:432px;border-radius:50%;border:2px solid rgba(255,255,255,.8);
  background:radial-gradient(circle,#fff2dc 0,#ffb38a 16%,#d85a7d 34%,#5a3aa0 62%,#2b2a7a 100%)}

/* footer */
.site-footer{position:absolute;left:0;top:4550px;width:1200px;height:289px;background:var(--navy-deep)}
.footer-brand{position:absolute;left:0;top:74px;width:1200px;text-align:center;font-family:var(--head);font-size:26px;letter-spacing:.5px}
.footer-item{position:absolute;top:153px;display:flex;align-items:center;gap:16px;font-size:10.5px;line-height:14px}
.footer-item .dot{width:30px;height:30px;border-radius:50%;background:var(--cream);display:flex;align-items:center;justify-content:center}
.footer-rule{position:absolute;left:66px;top:215px;width:1068px;height:1px;background:rgba(255,255,255,.45)}
.copyright{position:absolute;left:135px;top:240px;font-size:9.5px}
.socials{position:absolute;left:978px;top:235px;display:flex;gap:8px}
.socials span{width:24px;height:24px;border-radius:50%;border:1.5px solid var(--white);display:block}
</style>
</head>
<body>

<header class="site-header">
  <div class="brand">WILLOW TIDE ASTROLOGY</div>
  <nav class="main-nav">
    <a class="active" href="#" style="left:0">HOME</a>
    <a href="#" style="left:84px">ABOUT</a>
    <a href="#" style="left:173px">READINGS</a>
    <a href="#" style="left:285px">BOOKING</a>
    <a href="#" style="left:391px">BLOG</a>
  </nav>
  <a class="btn nav-contact" href="#">CONTACT</a>
</header>

<section class="hero">
  <h1 class="section-title hero-title">WILLOW TIDE ASTROLOGY</h1>
  <p class="hero-sub">Discover Your Cosmic Path with Expert Astrology Guidance</p>
  <a class="btn hero-cta" href="#">Get Started <svg viewBox="0 0 10 14"><path d="M2 2l5 5-5 5" fill="none" stroke="currentColor" stroke-width="2"/></svg></a>
  <div class="abs hero-wheel" role="img" aria-label="Glowing zodiac wheel with the twelve sign symbols"></div>
  <svg class="swoosh" style="top:770px;height:170px" viewBox="0 0 1200 170" aria-hidden="true">
    <path d="M0 22 C250 110 520 170 1035 75 C560 190 260 150 0 62 Z" fill="var(--cream)"/>
  </svg>
</section>

<section class="about">
  <div class="abs about-ring"></div>
  <div class="abs about-art" role="img" aria-label="Vintage zodiac chart with a quill in the centre"></div>
  <h2 class="section-title about-title">ABOUT US</h2>
  <div class="divider" style="left:657px;top:1168px;width:125px"></div>
  <p class="about-text">Lorem ipsum dolor sit amet, consectetur adipiscing elit, sed do eiusmod tempor incididunt ut labore et dolore magna aliqua. Quis ipsum suspendisse ultrices gravida. Risus comm odo viverra maecenas accumsan lacus vel facilisis. Lorem ipsum dolor sit amet, consectetur adipiscing</p>
  <a class="btn about-cta" href="#">Learn More <svg viewBox="0 0 10 14"><path d="M2 2l5 5-5 5" fill="none" stroke="currentColor" stroke-width="2"/></svg></a>
</section>

<section class="fate">
  <div class="abs fate-band" role="img" aria-label="Violet band with a faint zodiac wheel and numbers"></div>
  <h2 class="section-title fate-title">LET THE STARS HELP YOU TO DISCOVER<br>YOUR FATE</h2>
  <div class="divider" style="left:536px;top:2000px;width:128px"></div>
  <p class="fate-text">Lorem ipsum dolor sit amet, consectetur adipiscing elit, sed do eiusmod tempor incididunt ut labore et dolore magna aliqua. Quis ipsum suspendisse ultrices gravida.</p>
  <a class="btn fate-cta" href="#">Get Your Horoscope Reading <svg viewBox="0 0 10 14"><path d="M2 2l5 5-5 5" fill="none" stroke="currentColor" stroke-width="2"/></svg></a>
</section>

<section class="services">
  <h2 class="section-title" style="left:0;width:1200px;text-align:center;top:2556px;font-size:36px">OUR SERVICES</h2>
  <div class="divider" style="left:536px;top:2625px;width:128px"></div>
  <article class="card" style="left:66px">
    <div class="card-icon" role="img" aria-label="Line drawing of a sun with rays"></div>
    <h3>General Consultation</h3>
    <p style="top:226px">Lorem ipsum dolor sit amet, consectetur adipiscing elit, sed do eiusmod tempor incididunt ut labore et dolore</p>
  </article>
  <article class="card" style="left:434px">
    <div class="card-icon" role="img" aria-label="Line drawing of an open hand"></div>
    <h3>Personalized Readings</h3>
    <p style="top:226px">Lorem ipsum dolor sit amet, consectetur adipiscing elit, sed do eiusmod tempor incididunt ut labore et dolore</p>
  </article>
  <article class="card" style="left:806px">
    <div class="card-icon" role="img" aria-label="Line drawing of a sparkling star"></div>
    <h3>Work, Career &amp; Finance Reading</h3>
    <p style="top:244px">Lorem ipsum dolor sit amet, consectetur adipiscing elit, sed do eiusmod</p>
  </article>
  <a class="btn services-cta" href="#">Book Now <svg viewBox="0 0 10 14"><path d="M2 2l5 5-5 5" fill="none" stroke="currentColor" stroke-width="2"/></svg></a>
</section>

<section class="blog">
  <h2 class="section-title" style="left:0;width:1200px;text-align:center;top:3284px;font-size:36px">LATEST BLOG</h2>
  <div class="divider" style="left:536px;top:3352px;width:128px"></div>

  <div class="post-img" style="left:71px;background:linear-gradient(180deg,#f0a040 0,#f7c060 45%,#c2602a 70%,#3a2a30 100%)" role="img" aria-label="Friends raising their arms at a sunset beach"></div>
  <article class="post-body" style="left:118px">
    <div class="post-date"><i></i>MAY 20, 2024</div>
    <h3>Lorem ipsum dolor sit amet. Sed pari atur accusamus est volup</h3>
    <p>Lorem ipsum dolor sit amet, con nsectetur adipiscing elit, sed do</p>
    <span class="post-more">READ MORE</span>
  </article>

  <div class="post-img" style="left:436px;background:linear-gradient(135deg,#f05a8a 0,#f48a9a 40%,#e8c8b8 70%,#b09a90 100%)" role="img" aria-label="Couple with a zodiac wheel in the background"></div>
  <article class="post-body" style="left:483px">
    <div class="post-date"><i></i>SEP 20, 2024</div>
    <h3>Lorem ipsum dolor sit amet. Sed pari atur accusamus est volup</h3>
    <p>Lorem ipsum dolor sit amet, con nsectetur adipiscing elit, sed do</p>
    <span class="post-more">READ MORE</span>
  </article>

  <div class="post-img" style="left:808px;background:linear-gradient(180deg,#6c7e90 0,#aab4bc 50%,#8a9aa8 100%)" role="img" aria-label="Woman reaching up toward a cloudy sky"></div>
  <article class="post-body" style="left:855px">
    <div class="post-date"><i></i>OCT 30, 2024</div>
    <h3>Lorem ipsum dolor sit amet. Sed pari atur accusamus est volup</h3>
    <p>Lorem ipsum dolor sit amet, con nsectetur adipiscing elit, sed do</p>
    <span class="post-more">READ MORE</span>
  </article>
</section>

<section class="contact">
  <div class="abs contact-bg"></div>
  <svg class="swoosh" style="top:3975px;height:160px" viewBox="0 0 1200 160" aria-hidden="true">
    <path d="M0 160 C200 40 420 0 650 10 C880 20 1080 70 1200 120 L1200 155 C1080 90 880 38 650 28 C430 18 220 50 0 160 Z" fill="var(--cream)"/>
    <path d="M0 160 C220 50 430 18 650 28 C880 38 1080 90 1200 155 L1200 0 L0 0 Z" fill="var(--navy-deep)"/>
  </svg>
  <h2 class="section-title contact-title">CONTACT US</h2>
  <div class="abs" style="left:70px;top:4174px;width:62px;height:2px;background:var(--cream-line)"></div>
  <div class="abs" style="left:72px;top:4170px;width:10px;height:10px;border-radius:50%;background:var(--cream)"></div>
  <p class="contact-intro">For more information, please fill out the following<br>and we will be touch in shortly</p>
  <div class="field" style="left:66px;top:4293px;width:281px;height:49px">First Name*</div>
  <div class="field" style="left:361px;top:4293px;width:279px;height:49px">Last Name</div>
  <div class="field" style="left:66px;top:4357px;width:281px;height:47px">Email Address*</div>
  <div class="field" style="left:361px;top:4357px;width:279px;height:47px">Subject*</div>
  <div class="field msg" style="left:66px;top:4421px;width:574px;height:58px">Message*</div>
  <a class="btn submit" href="#">Submit</a>
  <div class="abs contact-orb" role="img" aria-label="Open book beneath a glowing zodiac wheel"></div>
</section>

<footer class="site-footer">
  <div class="footer-brand">WILLOW TIDE ASTROLOGY</div>
  <div class="footer-item" style="left:266px">
    <span class="dot"><svg width="14" height="14" viewBox="0 0 24 24"><path d="M6.6 10.8a15 15 0 006.6 6.6l2.2-2.2a1 1 0 011-.25 11.4 11.4 0 003.6.57 1 1 0 011 1V20a1 1 0 01-1 1A17 17 0 013 4a1 1 0 011-1h3.5a1 1 0 011 1 11.4 11.4 0 00.57 3.6 1 1 0 01-.25 1z" fill="var(--ink)"/></svg></span>
    <span>CALL US<br>044 555 0192</span>
  </div>
  <div class="footer-item" style="left:459px">
    <span class="dot"><svg width="14" height="12" viewBox="0 0 24 18"><rect x="1" y="1" width="22" height="16" rx="2" fill="var(--ink)"/><path d="M2 2l10 8 10-8" fill="none" stroke="var(--cream)" stroke-width="2"/></svg></span>
    <span>EMAIL US<br>hello@willowtide.example</span>
  </div>
  <div class="footer-item" style="left:717px">
    <span class="dot"><svg width="12" height="15" viewBox="0 0 20 26"><path d="M10 0a9 9 0 00-9 9c0 7 9 17 9 17s9-10 9-17a9 9 0 00-9-9z" fill="var(--ink)"/><circle cx="10" cy="9" r="3.5" fill="var(--cream)"/></svg></span>
    <span>12 Harbour Lane, Eastmere<br>Willow Bay District</span>
  </div>
  <div class="footer-rule"></div>
  <p class="copyright">Copyright © 2024 All Rights Reserved By Company Name</p>
  <div class="socials" aria-label="Social links"><span></span><span></span><span></span></div>
</footer>

</body>
</html>
```